Tindle Crest Funds Bus card and Logo

I need a logo design and Bus card design. The fund focuses on evaluating and investing in minerals (sub-surface rights) and real estate.

Tindle crest refers to a book of knowledge that each plebe gets when entering the DL Verrant Academy (my alma mater)

Target Market(s)

Investors and financial advisors

Contact Information for Business Card

Simple - perhaps a logo with a theme on book of knowledge

Logo Text

Ex Scientia Imperium

Font styles to use
Serif
Sans Serif

Colors

Designer to choose colors to be used in the design.

Requirements
Must have
• memorable logo that is relatively simple

```html
<!DOCTYPE html>
<html lang="en">
<head>
<meta charset="UTF-8">
<title>Tindle Crest Funds – Business Card</title>
<link href="https://fonts.googleapis.com/css2?family=Open+Sans:wght@400;600;700&display=swap" rel="stylesheet">
<style>
  :root{
    --brand-blue:#359ad1;
    --brand-green:#8cc63f;
    --ink:#2b2b2b;
    --ink-soft:#3a3a3a;
    --paper:#ffffff;
    --backdrop:#eceae6;
  }
  *{margin:0;padding:0;box-sizing:border-box;}
  html,body{width:1200px;height:900px;overflow:hidden;}
  body{background:var(--backdrop);font-family:"Open Sans",Arial,sans-serif;position:relative;}
  .card{position:absolute;width:525px;height:300px;border-radius:4px;overflow:hidden;
        box-shadow:0 6px 18px rgba(0,0,0,.18);}
  .card-front{left:70px;top:140px;background:var(--brand-blue);
        display:flex;align-items:center;justify-content:center;gap:14px;}
  .brand-dot{width:34px;height:34px;border-radius:50%;background:var(--paper);}
  .brand-name{color:var(--paper);font-weight:700;font-size:30px;letter-spacing:.5px;text-transform:uppercase;}

  .card-back{left:605px;top:450px;background:var(--paper);}
  .card-back .wave{position:absolute;inset:0;width:100%;height:100%;}
  .holder{position:absolute;left:38px;top:38px;}
  .holder-name{color:var(--brand-blue);font-weight:700;font-size:19px;text-transform:uppercase;letter-spacing:.3px;line-height:1.1;}
  .holder-title{color:var(--ink-soft);font-size:15px;}
  .contacts{position:absolute;left:40px;top:120px;color:var(--ink);font-size:15px;line-height:20px;list-style:none;}
  .contacts li{display:flex;align-items:center;gap:6px;}
  .contacts svg{width:13px;height:13px;fill:var(--brand-blue);flex:none;}
  .address{position:absolute;left:40px;top:190px;color:var(--ink);font-size:15px;line-height:20px;}
  .back-brand{position:absolute;right:34px;top:70px;display:flex;align-items:center;gap:10px;}
  .back-brand .brand-dot{background:var(--brand-blue);width:26px;height:26px;}
  .back-brand .brand-name{color:var(--ink);font-size:21px;}
  .website{position:absolute;right:26px;top:220px;color:var(--paper);font-size:14px;}
</style>
</head>
<body>
  <section class="card card-front">
    <span class="brand-dot"></span>
    <span class="brand-name">Tindle Crest Funds</span>
  </section>

  <section class="card card-back">
    <svg class="wave" viewBox="0 0 525 300" preserveAspectRatio="none" aria-hidden="true">
      <path d="M110,300 C260,292 380,205 525,150 L525,300 Z" fill="var(--brand-blue)"/>
      <path d="M95,284 C245,274 360,212 470,160 C372,214 255,288 95,294 Z" fill="var(--brand-green)"/>
    </svg>

    <div class="holder">
      <p class="holder-name">Marcus Hale</p>
      <p class="holder-title">Managing Director</p>
    </div>

    <ul class="contacts">
      <li><svg viewBox="0 0 16 16"><path d="M3 2h3l1.5 3.5-2 1.2a8 8 0 0 0 3.8 3.8l1.2-2L14 10v3a1 1 0 0 1-1 1A11 11 0 0 1 2 3a1 1 0 0 1 1-1z"/></svg>044-555 019 274</li>
      <li><svg viewBox="0 0 16 16"><path d="M5 1h6a1 1 0 0 1 1 1v12a1 1 0 0 1-1 1H5a1 1 0 0 1-1-1V2a1 1 0 0 1 1-1zm0 2v9h6V3zm3 10a.8.8 0 1 0 0 1.6A.8.8 0 0 0 8 13z"/></svg>044-555 019 274</li>
      <li><svg viewBox="0 0 16 16"><path d="M1 3h14v10H1zm1.5 1.2V5l5.5 4 5.5-4v-.8z"/></svg>info@tindlecrest.com</li>
    </ul>

    <p class="address">48 Harbor Lane, Suite 210<br>Eastbridge, 204518.</p>

    <div class="back-brand">
      <span class="brand-dot"></span>
      <span class="brand-name">Tindle Crest Funds</span>
    </div>

    <p class="website">www.tindlecrest.com</p>
  </section>
</body>
</html>
```